Nutritional Supplement Brand in Need of a Website Cleanse!

We are in need of a website overhaul, one that will make our product, which is a healthy greens powder supplement, appear more sophisticated and appealing. Up till now most of our efforts have focused on formulating the product and setting up distribution. We did go down the internet marketing / pagetrellis selling path without too much success. What we'd like to do now is really bring focus to the benefits of the product, the ingredients, the value proposition. We would like green designs that accentuate the healthy energy and benefits the product drives (a very fresh, clean and energetic feel).
Updates

Project Deadline Extended
Reason: Extending the deadline out 5 days since I was late in providing feedback and because so many great designs were submitted. Thanks for your patience and understanding.

Target Market(s)

People who suffer from low energy levels and those who live a very active lifestyle and are in search of ways to boost their energy in a healthy way (not through coffee or sugary energy drinks). Primarily M/F in the 25-45 age range. Also people who know that they need to eat more fruits and vegetables on a daily basis but have neither the time or the money to do so.

Industry/Entity Type

Health And Wellness

Number of Pages Required

1 page

Font styles to use
Sans Serif

Colors
cadf82
acd036
b5d664
eaf2ce

Requirements
Must have
• My site is currently in Wordpress and can be seen at http://www.verdalux42blend.example
• The product can also be found on Shopzenta at https://www.shopzenta.example/dp/K73QWERT2L
• I would like the site to remain in Wordpress and will pay extra to have the layout coded into Wordpress although this isn't a requirement for proposals.
• Here are some examples of sites around my niche that I like the look and feel of:
• http://www.plumevita.example/2-classic-cb/
• https://vigorleafusa.example/
• https://www.brightmeadow.example/
• http://kelvaroot.example/turmeric/
• My current site is in the layout of a long-form sales letter. I don't want the new design to be so sales-pitch in manner. I want it to be more about the energy-driving benefits of the core ingredients in the formula and testimonials (designs can leverage some that are on my existing site and positive reviews on the Shopzenta listing). My current site leads with a video but this is not necessary in the redesign. I do have an edited video that's 2-3 minutes long that could be leveraged if a designer wanted to go down this path (it's absolutely not necessary though). I plan to utilize social media influencers to drive traffic to my listing so I'm hoping this will allow for a bit less sales-pitch needed on the site itself. Using all of the copy that's on the existing website in not necessary, a lot of it is redundant and it's in need of an overhaul. I'd rather slim down the site and keep it very product-focused.
• In terms of social media I'd like a link to my pictogrove and friendlane pages:
• https://www.pictogrove.example/verdalux42blend/
• https://www.friendlane.example/V42Blend/
• I want the site to be responsive and look great on all devices (desktop, mobile).
• I'm new to artmingle so please hit me up with further questions if needed.
Nice to have
• Would love a new look and feel to my logo. I'm not a huge fan of the current one. I can't really change the name of the product at this point but the logo on the site can be edited and a new look is encouraged.

```html
<!DOCTYPE html>
<html lang="en">
<head>
<meta charset="utf-8">
<title>Verdalux 42 Blend — Website Layout</title>
<link rel="stylesheet" href="https://fonts.googleapis.com/css2?family=Montserrat:wght@400;500;600;700&family=Lato:wght@300;400&display=swap">
<style>
  :root{
    --stage:#333333;
    --white:#ffffff;
    --ink:#1c1c1c;
    --muted:#8a8a8a;
    --soft:#b4b4b4;
    --band:#e3e3e3;
    --panel:#e6e6e6;
    --hero-dark:#050505;
    --hero-mid:#2a2a2a;
    --lime:#acd036;
    --lime-soft:#b5d664;
  }
  *{margin:0;padding:0;box-sizing:border-box}
  html,body{width:1200px;height:1200px;overflow:hidden;background:var(--stage)}
  body{position:relative;font-family:"Lato",sans-serif;color:var(--ink)}
  .screen{position:absolute;background:var(--white);overflow:hidden}
  .screen--desktop{left:233px;top:62px;width:534px;height:1075px}
  .screen--mobile{left:820px;top:62px;width:147px;height:1075px}
  .abs{position:absolute}
  .center{left:0;right:0;text-align:center}
  .logo{font-family:"Montserrat",sans-serif;font-weight:700;color:var(--ink);line-height:1;letter-spacing:.2px}
  .hero{background:radial-gradient(ellipse at 70% 45%,var(--hero-mid) 0%,var(--hero-dark) 70%)}
  .hero-kicker{font-family:"Montserrat",sans-serif;font-weight:400;color:var(--white);letter-spacing:.5px}
  .hero-title{font-family:"Montserrat",sans-serif;font-weight:600;color:var(--white);letter-spacing:1.2px;line-height:1.08;white-space:nowrap}
  .hero-sub{font-family:"Lato",sans-serif;color:#d8d8d8;letter-spacing:.5px;line-height:1.6;text-transform:uppercase}
  .btn-outline{border:1px solid var(--white);border-radius:3px;color:var(--white);font-family:"Montserrat",sans-serif;font-weight:600;letter-spacing:1px;display:flex;align-items:center;justify-content:center}
  .btn-outline--dark{border-color:var(--ink);color:var(--ink)}
  .btn-lime{background:var(--lime);color:var(--white);border-radius:2px;font-family:"Montserrat",sans-serif;font-weight:600;letter-spacing:1px;display:flex;align-items:center;justify-content:center}
  .product-shot{background:linear-gradient(180deg,#f2f2f2 0%,#f2f2f2 12%,#1a1a1a 14%,#2f5a24 45%,#1a1a1a 82%,#e8e8e8 84%,#ffffff 100%);border-radius:4px}
  .dots{display:flex;gap:4px;justify-content:center}
  .dot{width:4px;height:4px;border-radius:50%;border:1px solid #bbb}
  .dot--on{background:var(--white);border-color:var(--white)}
  .dots--dark .dot{border-color:#777}
  .dots--dark .dot--on{background:var(--ink);border-color:var(--ink)}
  .tagline-band{background:var(--band)}
  .tagline{font-size:7px;letter-spacing:.8px;color:#777;text-transform:uppercase;transform:translateX(-50%);white-space:nowrap}
  .quote-kicker{font-size:7px;letter-spacing:.9px;color:#666;text-transform:uppercase}
  .quote-line{font-family:"Montserrat",sans-serif;font-weight:500;letter-spacing:1.4px;text-transform:uppercase;color:var(--ink)}
  .quote-cite{font-size:5px;letter-spacing:.6px;color:#999;text-transform:uppercase}
  .link-lime{font-family:"Montserrat",sans-serif;font-size:5px;letter-spacing:1px;color:var(--lime);text-transform:uppercase}
  .link-lime--under{text-decoration:underline}
  .panel{background:var(--panel)}
  .compare-title{font-family:"Montserrat",sans-serif;font-weight:400;letter-spacing:1.2px;text-transform:uppercase;color:#333}
  .compare-title b{font-weight:700}
  .feature{transform:translateX(-50%);text-align:center}
  .feature-icon{display:block;margin:0 auto}
  .feature-label{font-size:5px;color:var(--soft);line-height:1.5;margin-top:3px;white-space:nowrap}
  .section-title{font-family:"Montserrat",sans-serif;font-weight:500;letter-spacing:1.6px;text-transform:uppercase;color:var(--ink)}
  .card{background:var(--white);border:1px solid #eeeeee}
  .card-photo{width:100%}
  .card-title{font-family:"Montserrat",sans-serif;font-size:6.4px;letter-spacing:1px;text-transform:uppercase;text-align:center;color:var(--ink)}
  .card-text{font-size:4.9px;line-height:1.65;color:#9a9a9a;text-align:center;letter-spacing:.3px}
  .faded{opacity:.45}
</style>
</head>
<body>

<main class="screen screen--desktop">
  <header>
    <div class="abs logo" style="left:13px;top:10px;font-size:6.5px">VERDALUX 42<br><span style="font-size:9px">BLEND</span></div>
    <div class="abs" style="left:330px;top:19px;font-size:5.5px;color:#999;letter-spacing:.4px">Join / Log In To V42B Account</div>
    <div class="abs btn-outline btn-outline--dark" style="left:465px;top:11px;width:60px;height:17px;font-size:5.5px">BUY NOW</div>
  </header>

  <section class="abs hero" style="left:0;top:38px;width:534px;height:227px">
    <div class="abs hero-kicker" style="left:59px;top:39px;font-size:13px">THIS IS</div>
    <div class="abs hero-title" style="left:59px;top:56px;font-size:26px">VERDALUX<br>42 BLEND</div>
    <div class="abs hero-sub" style="left:60px;top:120px;font-size:6.4px">8 Miracle ingredients.<br>20 servings of fruits &amp; veggies daily.</div>
    <div class="abs btn-outline" style="left:59px;top:160px;width:71px;height:17px;font-size:5.6px">SHOP NOW</div>
    <div class="abs product-shot" role="img" aria-label="Three tubs of the greens powder, centre tub in front" style="left:298px;top:25px;width:179px;height:169px;border-radius:8px"></div>
    <div class="abs dots center" style="top:212px"><span class="dot dot--on"></span><span class="dot"></span><span class="dot"></span></div>
  </section>

  <section class="abs tagline-band" style="left:0;top:265px;width:534px;height:28px">
    <span class="abs tagline" style="left:82px;top:10px">Stay alert.</span>
    <span class="abs tagline" style="left:270px;top:10px">Stay focused.</span>
    <span class="abs tagline" style="left:443px;top:10px">Stay energized.</span>
  </section>

  <section class="abs" style="left:0;top:293px;width:534px;height:197px">
    <div class="abs center quote-kicker" style="top:59px">Verdalux 42 Blend is the</div>
    <div class="abs center quote-line" style="top:75px;font-size:13.5px;line-height:1.45">"Pinnacle of healthy drinks,<br>taste's great and mixes easily"</div>
    <div class="abs center quote-cite" style="top:123px">-Marisol Dentley, #1 health and wellness channel on Vidora</div>
    <div class="abs center link-lime" style="top:150px">Watch video</div>
  </section>

  <section class="abs panel" style="left:0;top:490px;width:534px;height:226px">
    <div class="abs product-shot" role="img" aria-label="Single tub of the greens powder" style="left:74px;top:30px;width:112px;height:168px;border-radius:10px"></div>
    <div class="abs compare-title" style="left:234px;top:61px;font-size:12px;line-height:1.55">How <b>Verdalux 42 Blend</b> is<br>different from other products?</div>

    <div class="abs feature" style="left:246px;top:114px">
      <svg class="feature-icon" width="25" height="25" viewBox="0 0 24 24"><circle cx="12" cy="12" r="11" fill="#fff" stroke="#c8c8c8" stroke-width="1"/><path d="M12 5l1.6 3 2.4-1-.6 3 2.6.4-2 2.2 1 1.4-3 .2.2 3H12.8v2.4h-1.6V17.2H9.8l.2-3-3-.2 1-1.4-2-2.2 2.6-.4-.6-3 2.4 1z" fill="#8a8a8a"/></svg>
      <div class="feature-label">All Natural</div>
    </div>
    <div class="abs feature" style="left:299px;top:114px">
      <svg class="feature-icon" width="25" height="25" viewBox="0 0 24 24"><circle cx="12" cy="12" r="11" fill="#fff" stroke="#c8c8c8" stroke-width="1"/><circle cx="12" cy="13.5" r="4.6" fill="#8a8a8a"/><path d="M12 9c.4-1.6 1.4-2.4 2.8-2.6" stroke="#8a8a8a" stroke-width="1" fill="none"/></svg>
      <div class="feature-label">20 Servings<br>of Fruit</div>
    </div>
    <div class="abs feature" style="left:353px;top:114px">
      <svg class="feature-icon" width="25" height="25" viewBox="0 0 24 24"><circle cx="12" cy="12" r="11" fill="#fff" stroke="#c8c8c8" stroke-width="1"/><path d="M10.4 6.5h3.2v4h4v3.2h-4v4h-3.2v-4h-4v-3.2h4z" fill="#8a8a8a"/></svg>
      <div class="feature-label">Total Health</div>
    </div>
    <div class="abs feature" style="left:406px;top:114px">
      <svg class="feature-icon" width="25" height="25" viewBox="0 0 24 24"><circle cx="12" cy="12" r="11" fill="#fff" stroke="#c8c8c8" stroke-width="1"/><path d="M9 11V8a2.2 2.2 0 0 1 4.4 0" stroke="#8a8a8a" stroke-width="1.2" fill="none"/><rect x="10.5" y="11" width="6" height="6" rx=".8" fill="#8a8a8a"/></svg>
      <div class="feature-label">Non-addicting</div>
    </div>
    <div class="abs feature" style="left:460px;top:114px">
      <svg class="feature-icon" width="25" height="25" viewBox="0 0 24 24"><circle cx="12" cy="12" r="11" fill="#fff" stroke="#c8c8c8" stroke-width="1"/><rect x="6" y="9" width="12" height="6" rx="3" fill="#8a8a8a"/></svg>
      <div class="feature-label">60 Synergistic<br>Ingredients</div>
    </div>
  </section>

  <section class="abs" style="left:0;top:716px;width:534px;height:359px">
    <h2 class="abs center section-title" style="top:38px;font-size:13px">Stay Focused</h2>

    <article class="abs card faded" style="left:-95px;top:83px;width:137px;height:201px">
      <div class="card-photo" role="img" aria-label="Athlete portrait, soft light backdrop" style="height:114px;background:linear-gradient(135deg,#d9d9d9,#a9aaa8)"></div>
      <div class="card-title" style="margin-top:11px">Strongman Competitor</div>
      <p class="card-text" style="margin:8px 10px 0">"Helps me get in the vitamins, minerals, and probiotics my body needs to power through training and shorten recovery time"</p>
    </article>

    <article class="abs card" style="left:53px;top:83px;width:137px;height:201px">
      <div class="card-photo" role="img" aria-label="Firefighter in gear holding a hose outdoors" style="height:114px;background:linear-gradient(160deg,#6f8a54 0%,#96a472 45%,#7b6a3a 100%)"></div>
      <div class="card-title" style="margin-top:11px">First Responders</div>
      <p class="card-text" style="margin:8px 10px 0">"It's important that I stay on top of my game health wise and since I've started taking Verdalux 42 Blend I've been able to do just that"</p>
    </article>

    <article class="abs card" style="left:200px;top:83px;width:137px;height:201px">
      <div class="card-photo" role="img" aria-label="Figure competitor flexing while holding the product tub, dark backdrop" style="height:114px;background:radial-gradient(ellipse at 50% 45%,#4a3a33 0%,#0d0d0d 70%)"></div>
      <div class="card-title" style="margin-top:11px">Figure Competitors</div>
      <p class="card-text" style="margin:8px 10px 0">"You absolutely must have a healthy body while training hard and this stuff will make sure your body is running at 100%"</p>
    </article>

    <article class="abs card" style="left:348px;top:83px;width:137px;height:201px">
      <div class="card-photo" role="img" aria-label="Strongman athlete in a gym beside a loaded barbell" style="height:114px;background:linear-gradient(180deg,#6b6560 0%,#4b4541 60%,#2e2a27 100%)"></div>
      <div class="card-title" style="margin-top:11px">Strongman Competitor</div>
      <p class="card-text" style="margin:8px 10px 0">"Helps me get in the vitamins, minerals, and probiotics my body needs to power through training and shorten recovery time"</p>
    </article>

    <article class="abs card faded" style="left:495px;top:83px;width:137px;height:201px">
      <div class="card-photo" role="img" aria-label="Athlete portrait, pale backdrop" style="height:114px;background:linear-gradient(135deg,#c9cfc9,#9fa7a0)"></div>
      <div class="card-title" style="margin-top:11px">First Responders</div>
      <p class="card-text" style="margin:8px 10px 0">"It's important that I stay on top of my game health wise and since I've started taking Verdalux 42 Blend I've been able to do just that"</p>
    </article>

    <div class="abs btn-lime" style="left:233px;top:318px;width:71px;height:15px;font-size:5.5px">TRY NOW</div>
  </section>
</main>

<main class="screen screen--mobile">
  <header>
    <div class="abs logo" style="left:11px;top:8px;font-size:5px">VERDALUX 42<br><span style="font-size:7px">BLEND</span></div>
    <svg class="abs" style="left:120px;top:10px" width="16" height="11" viewBox="0 0 16 11"><rect y="0" width="16" height="1.6" fill="#1c1c1c"/><rect y="4.7" width="16" height="1.6" fill="#1c1c1c"/><rect y="9.4" width="16" height="1.6" fill="#1c1c1c"/></svg>
  </header>

  <section class="abs hero" style="left:0;top:30px;width:147px;height:295px">
    <div class="abs center hero-kicker" style="top:20px;font-size:9px">THIS IS</div>
    <div class="abs center hero-title" style="top:33px;font-size:18px">VERDALUX<br>42 BLEND</div>
    <div class="abs center hero-sub" style="top:82px;font-size:4.6px">8 Miracle ingredients.<br>20 servings of fruits &amp; veggies daily.</div>
    <div class="abs product-shot" role="img" aria-label="Three tubs of the greens powder" style="left:24px;top:132px;width:98px;height:92px;border-radius:6px"></div>
    <div class="abs dots center" style="top:242px"><span class="dot dot--on" style="width:3px;height:3px"></span><span class="dot" style="width:3px;height:3px"></span><span class="dot" style="width:3px;height:3px"></span></div>
    <div class="abs btn-outline" style="left:44px;top:260px;width:59px;height:14px;font-size:4.8px">SHOP NOW</div>
  </section>

  <section class="abs" style="left:0;top:325px;width:147px;height:100px">
    <div class="abs center quote-kicker" style="top:25px;font-size:5px">Verdalux 42 Blend is the</div>
    <div class="abs center quote-line" style="top:35px;font-size:6.3px;line-height:1.55;font-weight:700;letter-spacing:.3px">"Pinnacle of healthy drinks,<br>taste's great and mixes easily"</div>
    <div class="abs center quote-cite" style="top:58px;font-size:4px">-Marisol Dentley</div>
    <div class="abs center link-lime link-lime--under" style="top:75px;font-size:4.5px">Watch video</div>
  </section>

  <section class="abs panel" style="left:0;top:425px;width:147px;height:373px">
    <div class="abs product-shot" role="img" aria-label="Single tub of the greens powder" style="left:41px;top:17px;width:65px;height:99px;border-radius:6px"></div>
    <div class="abs center compare-title" style="top:140px;font-size:5.6px;line-height:1.75;letter-spacing:.4px">How <b>Verdalux 42 Blend</b> is<br>different from other products?</div>

    <div class="abs feature" style="left:42px;top:175px">
      <svg class="feature-icon" width="27" height="27" viewBox="0 0 24 24"><circle cx="12" cy="12" r="11" fill="#fff" stroke="#c8c8c8" stroke-width="1"/><path d="M12 5l1.6 3 2.4-1-.6 3 2.6.4-2 2.2 1 1.4-3 .2.2 3H12.8v2.4h-1.6V17.2H9.8l.2-3-3-.2 1-1.4-2-2.2 2.6-.4-.6-3 2.4 1z" fill="#8a8a8a"/></svg>
      <div class="feature-label">All Natural</div>
    </div>
    <div class="abs feature" style="left:98px;top:175px">
      <svg class="feature-icon" width="27" height="27" viewBox="0 0 24 24"><circle cx="12" cy="12" r="11" fill="#fff" stroke="#c8c8c8" stroke-width="1"/><circle cx="12" cy="13.5" r="4.6" fill="#8a8a8a"/><path d="M12 9c.4-1.6 1.4-2.4 2.8-2.6" stroke="#8a8a8a" stroke-width="1" fill="none"/></svg>
      <div class="feature-label">20 Servings<br>of Fruit</div>
    </div>
    <div class="abs feature" style="left:42px;top:240px">
      <svg class="feature-icon" width="27" height="27" viewBox="0 0 24 24"><circle cx="12" cy="12" r="11" fill="#fff" stroke="#c8c8c8" stroke-width="1"/><path d="M10.4 6.5h3.2v4h4v3.2h-4v4h-3.2v-4h-4v-3.2h4z" fill="#8a8a8a"/></svg>
      <div class="feature-label">Total Health</div>
    </div>
    <div class="abs feature" style="left:98px;top:240px">
      <svg class="feature-icon" width="27" height="27" viewBox="0 0 24 24"><circle cx="12" cy="12" r="11" fill="#fff" stroke="#c8c8c8" stroke-width="1"/><path d="M9 11V8a2.2 2.2 0 0 1 4.4 0" stroke="#8a8a8a" stroke-width="1.2" fill="none"/><rect x="10.5" y="11" width="6" height="6" rx=".8" fill="#8a8a8a"/></svg>
      <div class="feature-label">Non-addicting</div>
    </div>
    <div class="abs feature" style="left:42px;top:300px">
      <svg class="feature-icon" width="27" height="27" viewBox="0 0 24 24"><circle cx="12" cy="12" r="11" fill="#fff" stroke="#c8c8c8" stroke-width="1"/><rect x="9.5" y="6.5" width="5" height="11" rx="1" fill="#8a8a8a"/></svg>
      <div class="feature-label">No Capsules</div>
    </div>
    <div class="abs feature" style="left:98px;top:300px">
      <svg class="feature-icon" width="27" height="27" viewBox="0 0 24 24"><circle cx="12" cy="12" r="11" fill="#fff" stroke="#c8c8c8" stroke-width="1"/><rect x="6" y="9" width="12" height="6" rx="3" fill="#8a8a8a"/></svg>
      <div class="feature-label">60 Synergistic<br>Ingredients</div>
    </div>
  </section>

  <section class="abs" style="left:0;top:798px;width:147px;height:277px">
    <h2 class="abs center section-title" style="top:23px;font-size:9.6px;letter-spacing:.8px">Stay Focused</h2>
    <article class="abs card" style="left:15px;top:47px;width:113px;height:164px">
      <div class="card-photo" role="img" aria-label="Figure competitor flexing while holding the product tub, dark backdrop" style="height:94px;background:radial-gradient(ellipse at 50% 45%,#4a3a33 0%,#0d0d0d 70%)"></div>
      <div class="card-title" style="margin-top:13px;font-size:5.6px">Figure Competitors</div>
      <p class="card-text" style="margin:6px 7px 0;font-size:4.3px">"You absolutely must have a healthy body while training hard and this stuff will make sure your body is running at 100%"</p>
    </article>
    <div class="abs dots dots--dark center" style="top:225px"><span class="dot dot--on" style="width:3px;height:3px"></span><span class="dot" style="width:3px;height:3px"></span><span class="dot" style="width:3px;height:3px"></span></div>
    <div class="abs btn-lime" style="left:44px;top:241px;width:59px;height:13px;font-size:4.8px">TRY NOW</div>
  </section>
</main>

</body>
</html>
```